Letterhead Design Project

Professional but modern letterhead.

Target Market(s)

mining companies

Industry/Entity Type

It Professional

Colors

Designer to choose colors to be used in the design.

```html
<!DOCTYPE html>
<html lang="en">
<head>
<meta charset="utf-8">
<title>KOVA Letterhead</title>
<link href="https://fonts.googleapis.com/css2?family=Open+Sans:wght@400;600;700&display=swap" rel="stylesheet">
<style>
  :root {
    --brand-blue: #0f4a96;
    --ink-grey: #4a4a4a;
    --paper: #ffffff;
    --mark-tint: #eceef5;
  }
  html, body {
    margin: 0;
    padding: 0;
    overflow: hidden;
    background: var(--paper);
  }
  .letterhead {
    position: relative;
    width: 1105px;
    height: 1200px;
    background: var(--paper);
    overflow: hidden;
    font-family: "Open Sans", Arial, sans-serif;
  }
  .contact-block {
    position: absolute;
    left: 70px;
    top: 80px;
    color: var(--ink-grey);
    font-size: 15px;
    line-height: 20px;
  }
  .contact-line {
    display: flex;
    align-items: center;
    gap: 8px;
  }
  .contact-icon {
    width: 13px;
    height: 13px;
    flex: none;
  }
  .contact-address {
    margin-top: 8px;
  }
  .brand-name {
    position: absolute;
    right: 110px;
    top: 110px;
    display: flex;
    align-items: center;
    gap: 12px;
    color: var(--brand-blue);
    font-weight: 600;
    font-size: 52px;
    letter-spacing: 1px;
    line-height: 1;
  }
  .brand-dot {
    width: 22px;
    height: 22px;
    border-radius: 50%;
    background: var(--brand-blue);
  }
  .brand-backdrop {
    position: absolute;
    left: 190px;
    top: 760px;
    color: var(--mark-tint);
    font-weight: 600;
    font-size: 240px;
    letter-spacing: 4px;
    line-height: 1;
  }
  .footer-wave {
    position: absolute;
    left: 0;
    bottom: 0;
    width: 1105px;
    height: 320px;
  }
  .footer-url {
    position: absolute;
    right: 60px;
    bottom: 62px;
    color: var(--paper);
    font-weight: 700;
    font-size: 24px;
  }
</style>
</head>
<body>
<main class="letterhead">
  <section class="contact-block">
    <div class="contact-line">
      <svg class="contact-icon" viewBox="0 0 13 13"><circle cx="6.5" cy="6.5" r="6.5" fill="var(--brand-blue)"/><path d="M4 3.5 L5.5 3.5 L6 5.5 L5 6.2 Q6 8 7 8.2 L7.8 7.2 L9.5 7.8 L9.5 9.3 Q6 9.8 3.8 5 Z" fill="#fff"/></svg>
      <span>555-210-4471</span>
    </div>
    <div class="contact-line">
      <svg class="contact-icon" viewBox="0 0 13 13"><circle cx="6.5" cy="6.5" r="6.5" fill="var(--brand-blue)"/><rect x="4.5" y="3" width="4" height="7" rx="0.8" fill="#fff"/></svg>
      <span>555-382-9016</span>
    </div>
    <div class="contact-line">
      <svg class="contact-icon" viewBox="0 0 13 13"><circle cx="6.5" cy="6.5" r="6.5" fill="var(--brand-blue)"/><rect x="3.5" y="4.5" width="6" height="4.5" fill="#fff"/></svg>
      <span>555-647-2258</span>
    </div>
    <div class="contact-line">
      <svg class="contact-icon" viewBox="0 0 13 13"><circle cx="6.5" cy="6.5" r="6.5" fill="var(--brand-blue)"/><rect x="3" y="4" width="7" height="5" fill="#fff"/><path d="M3 4 L6.5 7 L10 4" stroke="var(--brand-blue)" stroke-width="0.8" fill="none"/></svg>
      <span>office@Kovagroup.net</span>
    </div>
    <div class="contact-address">Suite # 418, Ridge Bldg, Ny 60219</div>
  </section>

  <header class="brand-name">
    <span class="brand-dot"></span>
    <span>KOVA</span>
  </header>

  <div class="brand-backdrop" aria-hidden="true">KOVA</div>

  <svg class="footer-wave" viewBox="0 0 1105 320" preserveAspectRatio="none" aria-hidden="true">
    <path d="M0,205 C200,330 460,300 700,185 C860,110 1000,72 1105,75 L1105,320 L0,320 Z" fill="var(--brand-blue)"/>
    <path d="M30,250 C230,330 470,305 705,200 C865,128 1000,92 1105,92" fill="none" stroke="var(--paper)" stroke-width="4"/>
  </svg>

  <div class="footer-url">www.Kovagroup.net</div>
</main>
</body>
</html>
```